2 x Digitize Logo | 2 x Business Cards | 2 x Fridge Magnets

We require 6 deliverables:
1. Residential logo redrawn (same just high quality for large print format).
2. Corporate logo redrawn (minor changes to wording and high quality for large print format).
3. New business card design for Furniture Removals (residential)
4. New business card design for Corporate Relocations (business)
5. New Fridge magnet for Furniture removals (residential)
6. New fridge magnet for Corporate Relocations (business)
1. Residential Logo
a. We require the logo to be translated into a high quality digital image with no modifications.
2. Residential Logo
a. We require the logo to be edited (add the word corporate relocations) be translated into a high quality digital image.
3. Using the resilogo please make a new business card for our business.
a. Please see the web site https://www.brightlanehaulage.com.au for colours and inspiration.
b. The residential business card needs the following information:
i. Business Name (using the residential logo).
ii. Free Call: 1800 BL Haul (the Q, P and Move much be the same colour as the logo).
iii. Website: www.BrightLaneHaulage.com.au
iv. Address: 4/7 Ashgrove Court, VIC 3521
v. Email: move@BrightLaneHaulage.com.au
vi. backof Card:
Review our service
www.RateYourStay.com.au
Services: Local, Country, Interstate | Furniture Removals | Piano, Billiard Tables & Antiques
4. Using the corplogo please make a new business card for our business.
b. The corporate business card needs the following information:
i. Business Name (using the corporate logo).
v. Email: corporate@BrightLaneHaulage.com.au
vi. Back of Card:
Review our service
www.RateYourStay.com.au
Services: Corporate relocations | Office equipment moves | Packing Service | Packing Materials
5. Using the resilogo please make a new fridge magent for our business.
b. The residential fidge magnet needs the following information:
iv. Services: Local, Country, Interstate | Furniture Removals | Piano, Billiard Tables & Antiques
6. Using the corplogo please make a new fridge magent for our business.
b. The corporate fidge magnet needs the following information:
iv. Services: Local, Country, Interstate | Corporate relocations
Target Market(s)
Residential Furniture Removals and Corporate Office relocations
Industry/Entity Type
Business
Contact Information for Business Card
Please see full brief for six items required
Requirements
Must have
- Clean simple, easy to read
Nice to have
- fresh, stand out, eye catching
Should not have
- plain, standard, boring, general

```html
<!DOCTYPE html>
<html lang="en">
<head>
<meta charset="utf-8">
<title>Bright Lane Haulage – Business Card</title>
<link rel="stylesheet" href="https://fonts.googleapis.com/css2?family=Roboto+Condensed:wght@700&display=swap">
<style>
  :root {
    --ink: #333333;
    --brand-yellow: #fdd132;
    --brand-red: #ed3237;
    --brand-green: #00a651;
    --paper: #ffffff;
    --rule: #333333;
  }
  html, body {
    margin: 0;
    padding: 0;
    width: 1200px;
    height: 1200px;
    overflow: hidden;
    background: var(--paper);
  }
  .sheet {
    position: relative;
    width: 1200px;
    height: 1200px;
    box-sizing: border-box;
    border: 1px solid var(--rule);
    font-family: "Roboto Condensed", "Arial Narrow", sans-serif;
    font-weight: 700;
    color: var(--ink);
  }
  .card {
    position: absolute;
    left: 185px;
    width: 830px;
    height: 460px;
    box-sizing: border-box;
    border: 1.5px solid var(--rule);
    background: var(--paper);
  }
  .card--front { top: 134px; }
  .card--back  { top: 606px; }

  .line {
    position: absolute;
    margin: 0;
    line-height: 1;
    white-space: nowrap;
  }

  /* Front */
  .brand-name {
    left: 42px;
    top: 96px;
    width: 744px;
    text-align: center;
    font-size: 78px;
    letter-spacing: -0.5px;
    color: var(--brand-green);
  }
  .free-call {
    left: 43px;
    top: 250px;
    font-size: 50px;
    letter-spacing: -0.5px;
  }
  .free-call .c-yellow { color: var(--brand-yellow); }
  .free-call .c-red    { color: var(--brand-red); }
  .free-call .c-green  { color: var(--brand-green); }
  .contact {
    left: 44px;
    font-size: 31px;
  }
  .contact--web   { top: 308px; }
  .contact--addr  { top: 350px; }
  .contact--email { top: 390px; }

  /* Back */
  .centered {
    left: 0;
    width: 100%;
    text-align: center;
  }
  .review-title { top: 87px;  font-size: 47px; }
  .review-url   { top: 153px; font-size: 47px; }
  .services-label { top: 275px; font-size: 32px; }
  .services-list  { font-size: 32px; }
  .services-list--one { top: 336px; }
  .services-list--two { top: 381px; }
</style>
</head>
<body>
  <div class="sheet">
    <section class="card card--front" aria-label="Card front">
      <h1 class="line brand-name">BRIGHT LANE HAULAGE</h1>
      <p class="line free-call">Free Call: 1800 <span class="c-yellow">B</span><span class="c-red">L</span> <span class="c-green">Haul</span></p>
      <p class="line contact contact--web">Website: www.BrightLaneHaulage.com.au</p>
      <p class="line contact contact--addr">Adress: 4/7 Ashgrove Court, VIC 3521</p>
      <p class="line contact contact--email">Email: move@BrightLaneHaulage.com.au</p>
    </section>

    <section class="card card--back" aria-label="Card back">
      <p class="line centered review-title">Review our service</p>
      <p class="line centered review-url">www.RateYourStay.com.au</p>
      <p class="line centered services-label">Services:</p>
      <p class="line centered services-list services-list--one">Local, Country, Interstate | Furniture Removals</p>
      <p class="line centered services-list services-list--two">Piano, Billiard Tables &amp; Antiques</p>
    </section>
  </div>
</body>
</html>
```